Fun, Colorful, Classy ,& Stylish Wine Bacholorette Labels

Thanks For Stopping By, My Hope is That we Can Knock this out of The Park :)
Ok, So Here is Our Big Idea.

We are going to be launching another product on zelvio that are similar to these below.
https://www.zelvio.com/Toast-Tags-Proposal-Soiree-Hen-Night/item/Q73KXW82PD/ref=lst_2_4?s=home-decor&ie=UTF8&qid=8846213057&sr=2-4&keywords=bridal+wine+labels&itemID=73pqRtuWmZa&preST=SY300_QL70&itemSrc=srch
https://www.zelvio.com/Wow-Look-Whos-Tying-Knot-Proposal/item/Q92MZL47VN/ref=rel_sim_41_3?_encoding=UTF8&rel_i=Q92MZL47VN&rel_r=KPWQX83JZL27NM46D19F&rel_w=tgQ4r&rel_wg=v9LpD&psc=1&refRID=KPWQX83JZL27NM46D19F
https://www.zelvio.com/Hen-Night-Nuptial-Vino-Flask-Tags/item/Q58TRW63KB/ref=rel_sim_41_2?_encoding=UTF8&rel_i=Q58TRW63KB&rel_r=KPWQX83JZL27NM46D19F&rel_w=tgQ4r&rel_wg=v9LpD&psc=1&refRID=KPWQX83JZL27NM46D19F

We are going to do a few Styles.
1 Bachelorette , Engagement Party - Bridal Gift - Funny - 6Pc

We are planning to do a few more but let’s start with this one first.

size: 4'' x 5'' - mock up should also be done on the bottle. pick from one of the quotes below and design a label that will knock our socks off. :)

the wine bottle pics are just an example of another company that have done something similar.

T

Industry/Entity Type

Wedding

Font styles to use
Script

Colors
e667a6
ffffff
33a6d7
b768aa
e34197
fbee3d
abd036
33b8a4
6b449b

Requirements
Must have
• Colorful Humor and tasteful
Nice to have
• a creative spin on concept
Should not have
• should not be plain jane/ boring.

```html
<!DOCTYPE html>
<html lang="en">
<head>
<meta charset="utf-8">
<title>Boom! He Put A Ring On It — Wine Label</title>
<link rel="stylesheet" href="https://fonts.googleapis.com/css2?family=Luckiest+Guy&display=swap">
<style>
  :root {
    --page-bg: #ffffff;
    --label-pink: #f6c1d3;
    --label-pink-deep: #efa9c3;
    --stripe-white: #fdf3f7;
    --hot-pink: #e34197;
    --soft-pink: #e667a6;
    --plum: #6b449b;
    --ring-gold: #fbee3d;
  }
  html, body {
    margin: 0;
    padding: 0;
    width: 1125px;
    height: 1200px;
    overflow: hidden;
    background: var(--page-bg);
  }
  .canvas {
    position: relative;
    width: 1125px;
    height: 1200px;
  }
  .wine-label {
    position: absolute;
    left: 122px;
    top: 50px;
    width: 880px;
    height: 1100px;
    box-shadow: 0 10px 30px rgba(0,0,0,0.12);
  }
  .wine-label svg { display: block; width: 100%; height: 100%; }
  .label-type {
    font-family: "Luckiest Guy", "Arial Black", sans-serif;
  }
  .type-shadow { fill: var(--plum); }
  .type-face {
    fill: var(--hot-pink);
    stroke: var(--plum);
    stroke-width: 4;
    paint-order: stroke;
  }
</style>
</head>
<body>
<main class="canvas">
  <section class="wine-label" aria-label="Bachelorette wine label">
    <svg viewBox="0 0 880 1100" xmlns="http://www.w3.org/2000/svg">
      <defs>
        <linearGradient id="label-wash" x1="0" y1="0" x2="1" y2="1">
          <stop offset="0" stop-color="var(--label-pink-deep)"/>
          <stop offset="0.5" stop-color="var(--label-pink)"/>
          <stop offset="1" stop-color="var(--label-pink-deep)"/>
        </linearGradient>
        <path id="arc-upper" d="M 120 600 Q 445 220 790 600"/>
        <path id="arc-lower" d="M 180 900 Q 420 1120 700 880"/>
      </defs>

      <rect class="label-ground" width="880" height="1100" fill="url(#label-wash)"/>

      <g class="label-stripes" fill="var(--stripe-white)">
        <rect x="0" y="160" width="880" height="22"/>
        <rect x="0" y="405" width="880" height="24"/>
        <rect x="0" y="645" width="880" height="24"/>
        <rect x="0" y="880" width="880" height="24"/>
      </g>

      <g class="headline label-type" font-size="190" text-anchor="middle">
        <text class="type-shadow" x="448" y="296">BOOM!</text>
        <text class="type-face" x="440" y="288">BOOM!</text>
      </g>

      <g class="arc-line label-type" font-size="125" text-anchor="middle">
        <text class="type-shadow" dx="6" dy="8"><textPath href="#arc-upper" startOffset="50%">HE PUT A</textPath></text>
        <text class="type-face"><textPath href="#arc-upper" startOffset="50%">HE PUT A</textPath></text>
      </g>

      <g class="ring-art" role="img" aria-label="Illustration of a gold engagement ring with a pink diamond and radiating sparkle lines">
        <rect x="290" y="510" width="250" height="330" rx="30" fill="var(--soft-pink)" opacity="0.35"/>
      </g>

      <g class="arc-line label-type" font-size="160" text-anchor="middle">
        <text class="type-shadow" dx="6" dy="8"><textPath href="#arc-lower" startOffset="50%">ON IT</textPath></text>
        <text class="type-face"><textPath href="#arc-lower" startOffset="50%">ON IT</textPath></text>
      </g>
    </svg>
  </section>
</main>
</body>
</html>
```